Criação de Logo e Cartao de Visita para Cordelina & Ribamar
A empresa queria:
" 1. Mote principal: venda de produtos ecológicos e divulgação de temas relacionados à preservação do meio ambiente e qualidade de vida. "

```html
<!DOCTYPE html>
<html lang="pt-BR">
<head>
<meta charset="utf-8">
<title>Cordelina &amp; Ribamar – Cartão de Visita</title>
<link rel="stylesheet" href="https://fonts.googleapis.com/css2?family=Varela+Round&display=swap">
<style>
  :root {
    --backdrop: #eceef2;
    --card-white: #ffffff;
    --forest: #2d5a2e;
    --forest-dark: #244a25;
    --lime: #8cc63f;
    --leaf: #5fae3a;
    --ink-light: #f4f7f0;
  }
  * { margin: 0; padding: 0; box-sizing: border-box; }
  html, body { width: 1200px; height: 1200px; overflow: hidden; }
  body {
    background: var(--backdrop);
    font-family: "Varela Round", sans-serif;
    position: relative;
  }
  .card {
    position: absolute;
    width: 900px;
    height: 500px;
    border-radius: 44px;
    left: 150px;
  }
  .card--front { top: 80px; background: var(--card-white); }
  .card--back  { top: 620px; background: var(--forest); color: var(--ink-light); }

  .brand {
    position: absolute;
    display: flex;
    flex-direction: column;
    align-items: flex-start;
  }
  .brand__row { display: flex; align-items: center; gap: 16px; }
  .brand__dot { width: 30px; height: 30px; border-radius: 50%; background: var(--leaf); }
  .brand__name { font-size: 54px; line-height: 1; }
  .brand__tagline {
    margin-top: 10px;
    margin-left: 46px;
    font-size: 15px;
    letter-spacing: 2px;
    color: var(--lime);
  }
  .card--front .brand { left: 200px; top: 200px; }
  .card--front .brand__name { color: var(--forest); }

  .card--back .brand { left: 360px; top: 310px; }
  .card--back .brand__name { color: var(--ink-light); font-size: 46px; }

  .tab {
    position: absolute;
    background: var(--lime);
    width: 16px;
  }
  .tab--left { left: -10px; top: 170px; height: 220px; border-radius: 8px 0 0 8px; }
  .tab--right { right: -10px; top: 70px; height: 100px; border-radius: 0 8px 8px 0; }

  .holder {
    position: absolute;
    right: 28px;
    top: 88px;
    text-align: right;
  }
  .holder__name { font-size: 26px; }
  .holder__role { font-size: 17px; margin-top: 6px; }

  .contacts {
    position: absolute;
    left: 32px;
    top: 185px;
    list-style: none;
  }
  .contacts__item {
    display: flex;
    align-items: flex-start;
    gap: 14px;
    font-size: 18px;
    margin-bottom: 22px;
    line-height: 1.15;
  }
  .contacts__icon {
    flex: none;
    width: 26px;
    height: 26px;
    border-radius: 50%;
    background: var(--lime);
  }
</style>
</head>
<body>

<section class="card card--front">
  <div class="brand">
    <div class="brand__row">
      <span class="brand__dot"></span>
      <span class="brand__name">Cordelina &amp; Ribamar</span>
    </div>
    <span class="brand__tagline">SUSTENTABILIDADE</span>
  </div>
</section>

<section class="card card--back">
  <span class="tab tab--left"></span>
  <span class="tab tab--right"></span>

  <div class="holder">
    <p class="holder__name">Nome Sobrenome</p>
    <p class="holder__role">Função/Cargo</p>
  </div>

  <ul class="contacts">
    <li class="contacts__item">
      <svg class="contacts__icon" viewBox="0 0 26 26" aria-hidden="true">
        <circle cx="13" cy="13" r="13" fill="#8cc63f"/>
        <path d="M9 7.5l2.5 2.5-1.5 1.8c.8 1.6 2 2.8 3.6 3.6l1.8-1.5 2.5 2.5-1.6 1.8c-4.2-.6-8.4-4.8-9-9z" fill="#2d5a2e"/>
      </svg>
      <span>(01) 5550-3148</span>
    </li>
    <li class="contacts__item">
      <span class="contacts__icon"></span>
      <span>/cordelinaribamar</span>
    </li>
    <li class="contacts__item">
      <span class="contacts__icon"></span>
      <span>@cordelinaribamar</span>
    </li>
    <li class="contacts__item">
      <svg class="contacts__icon" viewBox="0 0 26 26" aria-hidden="true">
        <circle cx="13" cy="13" r="13" fill="#8cc63f"/>
        <path d="M13 6a4.5 4.5 0 0 0-4.5 4.5c0 3.4 4.5 9 4.5 9s4.5-5.6 4.5-9A4.5 4.5 0 0 0 13 6z" fill="#2d5a2e"/>
        <circle cx="13" cy="10.5" r="1.7" fill="#8cc63f"/>
      </svg>
      <span>Rua das Palmeiras, 148<br>Centro - Vila Serena - SP</span>
    </li>
  </ul>

  <div class="brand">
    <div class="brand__row">
      <span class="brand__dot"></span>
      <span class="brand__name">Cordelina &amp; Ribamar</span>
    </div>
    <span class="brand__tagline">SUSTENTABILIDADE</span>
  </div>
</section>

</body>
</html>
```